Crestwell Renewal Business Card Design Phase 2

Professional and clean design. The design colors should flow with the logo. Two-sided card with the website on the back which is:

www.CrestwellRenewal.example.

"Specializing in Water Damage Restoration"

On the front I need the name, email, phone, and logo.

Name: Dorian Halvek
Email: Dorian@CrestwellRenewal.example
Phone: 555-318-2046 for now

I only have the Preview and Thumbnail right now but should have the source files uploaded within a day or two.

Target Market(s)

Flood victims, home owners with water damage from busted pipes etc...

Industry/Entity Type

Business

Contact Information for Business Card

Name: Dorian Halvek

Font styles to use
Serif
Sans Serif

Requirements
Must have
• Business Card Details Info

```html
<!DOCTYPE html>
<html lang="en">
<head>
<meta charset="utf-8">
<title>Crestwell Renewal Business Card</title>
<link href="https://fonts.googleapis.com/css2?family=Source+Sans+3:wght@400;600;700&display=swap" rel="stylesheet">
<style>
  :root {
    --backdrop: #3a322e;
    --card: #0c0c0c;
    --brand-blue: #2e4f8f;
    --brand-green: #4fa83a;
    --text-light: #f2f2f2;
  }
  * { margin: 0; padding: 0; box-sizing: border-box; }
  html, body {
    width: 1200px;
    height: 844px;
    overflow: hidden;
    background: var(--backdrop);
    font-family: "Source Sans 3", "Helvetica Neue", Arial, sans-serif;
  }
  .card-set {
    position: relative;
    width: 1200px;
    height: 844px;
  }
  .card {
    position: absolute;
    top: 268px;
    width: 540px;
    height: 309px;
    background: var(--card);
    box-shadow: 0 10px 30px rgba(0,0,0,0.45);
    overflow: hidden;
  }
  .card-front { left: 40px; }
  .card-back { left: 620px; }

  .brand-mark {
    display: flex;
    align-items: center;
    gap: 12px;
    font-weight: 700;
    font-size: 40px;
    line-height: 1;
    letter-spacing: 0.5px;
    text-transform: uppercase;
    color: var(--brand-blue);
  }
  .brand-dot {
    width: 22px;
    height: 22px;
    border-radius: 50%;
    background: var(--brand-green);
    flex: none;
  }

  /* Front */
  .card-front .brand-mark {
    position: absolute;
    left: 40px;
    top: 62px;
  }
  .name-rule {
    position: absolute;
    left: 0;
    top: 168px;
    width: 320px;
    height: 2px;
    background: var(--brand-green);
  }
  .holder-name {
    position: absolute;
    right: 40px;
    top: 154px;
    font-size: 22px;
    font-weight: 600;
    color: var(--brand-green);
  }
  .contact-list {
    position: absolute;
    right: 40px;
    top: 192px;
    list-style: none;
    text-align: right;
  }
  .contact-item {
    display: flex;
    justify-content: flex-end;
    align-items: center;
    gap: 8px;
    font-size: 17px;
    color: var(--text-light);
    margin-bottom: 9px;
  }
  .contact-icon { width: 14px; height: 14px; flex: none; }
  .base-rule {
    position: absolute;
    left: 0;
    right: 0;
    bottom: 40px;
    height: 2px;
    background: var(--brand-green);
  }

  /* Back */
  .card-back .brand-mark {
    position: absolute;
    left: 0;
    right: 0;
    top: 70px;
    justify-content: center;
  }
  .website {
    position: absolute;
    left: 0;
    right: 0;
    top: 150px;
    text-align: center;
    font-size: 17px;
    font-weight: 600;
    color: var(--brand-green);
  }
  .tagline-row {
    position: absolute;
    left: 0;
    right: 0;
    top: 212px;
    display: flex;
    align-items: center;
    gap: 14px;
  }
  .tagline-rule {
    flex: 1;
    height: 2px;
    background: var(--brand-green);
  }
  .tagline {
    font-size: 20px;
    font-weight: 600;
    color: var(--brand-green);
    white-space: nowrap;
  }
</style>
</head>
<body>
<main class="card-set">
  <section class="card card-front" aria-label="Card front">
    <div class="brand-mark"><span class="brand-dot"></span>Crestwell Renewal</div>
    <div class="name-rule"></div>
    <p class="holder-name">Dorian Halvek</p>
    <ul class="contact-list">
      <li class="contact-item">555-318-2046
        <svg class="contact-icon" viewBox="0 0 24 24" aria-hidden="true"><path fill="#4fa83a" d="M6.6 10.8a15.1 15.1 0 0 0 6.6 6.6l2.2-2.2a1 1 0 0 1 1-.25 11.4 11.4 0 0 0 3.6.57 1 1 0 0 1 1 1V20a1 1 0 0 1-1 1A17 17 0 0 1 3 4a1 1 0 0 1 1-1h3.5a1 1 0 0 1 1 1c0 1.25.2 2.45.57 3.57a1 1 0 0 1-.25 1z"/></svg>
      </li>
      <li class="contact-item">Dorian@CrestwellRenewal.example
        <svg class="contact-icon" viewBox="0 0 24 24" aria-hidden="true"><rect x="2" y="5" width="20" height="14" rx="1" fill="#4fa83a"/><path d="M3 6l9 7 9-7" stroke="#0c0c0c" stroke-width="1.8" fill="none"/></svg>
      </li>
    </ul>
    <div class="base-rule"></div>
  </section>

  <section class="card card-back" aria-label="Card back">
    <div class="brand-mark"><span class="brand-dot"></span>Crestwell Renewal</div>
    <p class="website">www.CrestwellRenewal.example</p>
    <div class="tagline-row">
      <span class="tagline-rule"></span>
      <p class="tagline">Specializing in Water Damage Restoration</p>
      <span class="tagline-rule"></span>
    </div>
  </section>
</main>
</body>
</html>
```